Veltrona stationery design

Design stationery for us that fits with the colours of the logo. We are looking for letterheads, business cards etc. Something we can use for a prospectus and marketing presentations in power point. Must be completed in such a manner that it represents a corporate image for large enterprise clients and other large organisations. The company is a project assurance and monitoring company that works in all industries.

```html
<!DOCTYPE html>
<html lang="en">
<head>
<meta charset="utf-8">
<title>Veltrona Letterhead</title>
<link href="https://fonts.googleapis.com/css2?family=Rubik:wght@400;600&display=swap" rel="stylesheet">
<style>
  :root {
    --backdrop: #8e8e8e;
    --paper: #ffffff;
    --header-bg: #000000;
    --brand-red: #f5210d;
    --brand-orange: #ff4a1c;
    --brand-blue: #033487;
    --text-light: #ffffff;
    --divider: #8a8a8a;
    --watermark: rgba(255, 110, 70, 0.18);
  }
  * { margin: 0; padding: 0; box-sizing: border-box; }
  html, body { width: 1200px; height: 1159px; overflow: hidden; }
  body {
    background: var(--backdrop);
    font-family: "Rubik", Arial, sans-serif;
    position: relative;
  }
  .letterhead {
    position: absolute;
    left: 211px;
    top: 30px;
    width: 778px;
    height: 1100px;
    background: var(--paper);
    overflow: hidden;
  }
  .letterhead__header {
    height: 150px;
    background: var(--header-bg);
    display: flex;
    align-items: center;
    padding: 0 40px 0 48px;
    color: var(--text-light);
  }
  .brand {
    display: flex;
    align-items: center;
    gap: 12px;
  }
  .brand__dot {
    width: 26px;
    height: 26px;
    border-radius: 50%;
    background: var(--brand-blue);
  }
  .brand__name {
    font-weight: 600;
    font-size: 27px;
    letter-spacing: 1px;
    text-transform: uppercase;
    color: var(--brand-orange);
  }
  .divider {
    width: 1px;
    height: 48px;
    background: var(--divider);
    margin: 0 24px;
  }
  .contact-group {
    display: flex;
    flex-direction: column;
    gap: 8px;
    font-size: 14px;
    letter-spacing: 0.4px;
  }
  .contact-item {
    display: flex;
    align-items: flex-start;
    gap: 9px;
    line-height: 1.1;
  }
  .contact-item svg { flex: none; width: 12px; height: 12px; margin-top: 1px; }
  .watermark {
    position: absolute;
    left: 0;
    right: 0;
    top: 470px;
    text-align: center;
    font-weight: 600;
    font-size: 120px;
    text-transform: uppercase;
    color: var(--watermark);
    letter-spacing: 4px;
  }
  .letterhead__footer {
    position: absolute;
    left: 0;
    bottom: 0;
    width: 778px;
    height: 40px;
  }
</style>
</head>
<body>
  <main class="letterhead">
    <header class="letterhead__header">
      <div class="brand">
        <span class="brand__dot"></span>
        <span class="brand__name">Veltrona</span>
      </div>
      <span class="divider"></span>
      <div class="contact-group">
        <div class="contact-item">
          <svg viewBox="0 0 12 12"><path d="M2.5 1 L4.5 1 L5.3 3.6 L4 4.6 Q5 7 7.4 8 L8.4 6.7 L11 7.5 L11 9.5 Q11 11 9.5 11 Q1 10.5 1 2.5 Q1 1 2.5 1Z" fill="var(--brand-red)"/></svg>
          <span>021-555 010 234</span>
        </div>
        <div class="contact-item">
          <svg viewBox="0 0 12 12"><rect x="0.5" y="2" width="11" height="8" fill="var(--brand-red)"/><path d="M0.5 2 L6 6.5 L11.5 2" stroke="#000" stroke-width="1" fill="none"/></svg>
          <span>hello@veltronamail.com</span>
        </div>
      </div>
      <span class="divider"></span>
      <div class="contact-group">
        <div class="contact-item">
          <svg viewBox="0 0 12 12"><circle cx="6" cy="6" r="5.5" fill="var(--brand-red)"/><path d="M0.5 6 H11.5 M6 0.5 Q3 6 6 11.5 M6 0.5 Q9 6 6 11.5" stroke="#000" stroke-width="0.8" fill="none"/></svg>
          <span>www.veltronagroup.com</span>
        </div>
        <div class="contact-item">
          <svg viewBox="0 0 12 12"><path d="M6 0.5 Q10 0.5 10 4.5 Q10 7.5 6 11.5 Q2 7.5 2 4.5 Q2 0.5 6 0.5Z" fill="var(--brand-red)"/><circle cx="6" cy="4.5" r="1.5" fill="#000"/></svg>
          <span>88, Harbour Street<br>Eastland, 30218</span>
        </div>
      </div>
    </header>

    <div class="watermark" aria-hidden="true">Veltrona</div>

    <svg class="letterhead__footer" viewBox="0 0 778 40" aria-hidden="true">
      <polygon points="0,24 470,24 454,40 0,40" fill="var(--brand-red)"/>
      <polygon points="484,24 778,24 778,40 468,40" fill="var(--brand-blue)"/>
    </svg>
  </main>
</body>
</html>
```